P&H RESTORATION

I want a brochure similiar to the example i've attached.
My company name is P&H Restoration. The website is: P-H-Restoration.com.
The phone number is 803.417.9056.

I don't like the "yellow" being the main color of the example so I'm open to suggestions. I want something CLEAN & Simple, like our logo . This will be a bi fold brochure

```html
<!DOCTYPE html>
<html lang="en">
<head>
<meta charset="UTF-8">
<title>P&amp;H Restoration – Bi-fold Brochure Spread</title>
<link rel="stylesheet" href="https://fonts.googleapis.com/css2?family=Barlow:wght@400;500;600;700&family=Barlow+Semi+Condensed:wght@500;600&display=swap">
<style>
  :root {
    --canvas: #d9d9dc;
    --ink: #1b1b1c;
    --ink-soft: #262628;
    --cyan: #38b3cc;
    --cyan-deep: #2a9db6;
    --white: #ffffff;
    --text-muted: #d7d7d7;
    --slate-1: #3c4352;
    --slate-2: #2a303c;
  }
  * { box-sizing: border-box; margin: 0; padding: 0; }
  html, body {
    width: 1200px; height: 840px; overflow: hidden;
    background: var(--canvas);
    font-family: "Barlow", Arial, sans-serif;
  }
  .spread {
    position: absolute; left: 40px; top: 30px;
    width: 1120px; height: 780px;
    display: flex;
    box-shadow: 0 12px 40px rgba(0,0,0,.25);
  }
  .panel { position: relative; width: 560px; height: 780px; overflow: hidden; }

  /* Inside-left panel */
  .panel--cover-photo {
    background: linear-gradient(150deg, var(--slate-1) 0%, #4a5161 45%, var(--slate-2) 100%);
  }

  /* Inside-right panel */
  .panel--services { background: var(--ink); }
  .panel-shapes { position: absolute; inset: 0; }

  .motto {
    position: absolute; left: 20px; top: 212px;
    color: var(--white);
    font-family: "Barlow Semi Condensed", Arial, sans-serif;
    font-weight: 500; font-size: 20px; letter-spacing: 5px; line-height: 1;
  }
  .motto span { display: block; padding: 6px 0; border-bottom: 1px solid rgba(255,255,255,.8); }
  .motto span:last-child { border-bottom: none; }
  .motto .m1 { padding-left: 28px; }

  .badge {
    position: absolute; left: 368px; top: 34px;
    width: 70px; height: 70px; border-radius: 50%;
    background: var(--cyan);
    display: flex; align-items: center; justify-content: center;
  }
  .headline {
    position: absolute; left: 170px; top: 118px; width: 370px;
    text-align: right;
  }
  .headline h1 {
    color: var(--white); font-weight: 700; font-size: 33px; line-height: 1.05;
  }
  .headline p {
    color: var(--cyan); font-weight: 400; font-size: 18px; margin-top: 2px; padding-right: 8px;
  }

  .benefits {
    position: absolute; left: 190px; top: 205px; width: 355px;
    display: grid; grid-template-columns: 1fr 1fr; column-gap: 18px; row-gap: 16px;
    align-items: start;
  }
  .benefit { display: flex; gap: 7px; }
  .benefit:nth-child(2) { margin-top: 34px; }
  .benefit:nth-child(3) { margin-top: -8px; }
  .benefit:nth-child(4) { margin-top: 22px; }
  .benefit-icon {
    flex: none; width: 20px; height: 20px; border-radius: 50%;
    background: var(--cyan); display: flex; align-items: center; justify-content: center;
  }
  .benefit h2 {
    color: var(--cyan); font-size: 10.5px; font-weight: 600; letter-spacing: .3px;
    text-transform: uppercase; margin: 3px 0 4px;
  }
  .benefit p { color: var(--text-muted); font-size: 9.5px; line-height: 1.35; }

  .feature-photo {
    position: absolute; left: 104px; top: 490px; width: 420px; height: 170px;
    background: linear-gradient(180deg, #b99b73 0%, #d9d4cc 40%, #2f4466 70%, #1e2b44 100%);
    box-shadow: 0 6px 18px rgba(0,0,0,.45);
  }

  .tagline {
    position: absolute; left: 140px; top: 680px;
    color: var(--white); font-size: 11px; font-weight: 500; letter-spacing: .4px; text-transform: uppercase;
  }
  .contact {
    position: absolute; left: 140px; top: 702px;
    color: var(--cyan); font-size: 11px; font-weight: 500; letter-spacing: .3px;
  }
  .brand {
    position: absolute; right: 40px; bottom: 44px;
    display: flex; align-items: center; gap: 8px;
    color: var(--white); font-size: 14px; font-weight: 500; letter-spacing: .5px;
  }
  .brand-mark { width: 10px; height: 10px; border: 1px solid var(--white); }
</style>
</head>
<body>
<main class="spread">

  <section class="panel panel--cover-photo" role="img" aria-label="Photo of rolled architectural blueprints under a dark slate-blue tint"></section>

  <section class="panel panel--services">
    <svg class="panel-shapes" width="560" height="780" viewBox="0 0 560 780" aria-hidden="true">
      <polygon points="0,0 175,0 0,175" fill="var(--ink-soft)"/>
      <polygon points="175,0 300,0 130,330 130,780 0,780 0,175" fill="var(--cyan)"/>
      <polygon points="0,175 90,175 0,250" fill="var(--cyan-deep)" opacity=".35"/>
    </svg>

    <div class="motto">
      <span class="m1">BUILD</span>
      <span class="m2">RENOVATE</span>
      <span class="m3">RESTORE</span>
    </div>

    <div class="badge" aria-hidden="true">
      <svg width="42" height="42" viewBox="0 0 42 42">
        <path d="M6 14 Q14 4 22 14 Z" fill="#fff"/>
        <line x1="14" y1="14" x2="14" y2="20" stroke="#fff" stroke-width="1.5"/>
        <path d="M10 26 L24 14 L38 26 Z" fill="#fff"/>
        <rect x="14" y="26" width="20" height="12" fill="#fff"/>
        <rect x="21" y="30" width="6" height="8" fill="var(--cyan)"/>
      </svg>
    </div>

    <header class="headline">
      <h1>Water or Mold Damage?</h1>
      <p>What happens after the cleanup?</p>
    </header>

    <div class="benefits">
      <article class="benefit">
        <span class="benefit-icon"><svg width="12" height="12" viewBox="0 0 12 12"><path d="M6 1 Q10 6 10 8 A4 4 0 0 1 2 8 Q2 6 6 1Z" fill="#fff"/></svg></span>
        <div><h2>1. Adjuster's Inspection</h2>
        <p>Feel Confident. Be sure you received a fair and accurate assessment &amp; repair of all damages with our team's use of industry leading Estimating Systems and On-Site Review.</p></div>
      </article>
      <article class="benefit">
        <span class="benefit-icon"><svg width="12" height="12" viewBox="0 0 12 12"><path d="M3 1 H9 L6 6 L9 11 H3 L6 6 Z" fill="#fff"/></svg></span>
        <div><h2>2. Timely Settlement</h2>
        <p>Don't wait. Minimize the hassle of long processing times from Estimate to Settlement when you team up with an Insurance Repair Specialist.</p></div>
      </article>
      <article class="benefit">
        <span class="benefit-icon"><svg width="12" height="12" viewBox="0 0 12 12"><path d="M1 6 L6 1.5 L11 6 H9.5 V11 H2.5 V6 Z" fill="#fff"/></svg></span>
        <div><h2>3. Under One Roof</h2>
        <p>Don't Worry. You won't need to arrange meetings with multiple contractors, we'll take care of everything from demo to final cleanup.</p></div>
      </article>
      <article class="benefit">
        <span class="benefit-icon"><svg width="12" height="12" viewBox="0 0 12 12"><path d="M2 2 L10 10 M10 2 L2 10" stroke="#fff" stroke-width="2"/></svg></span>
        <div><h2>4. Superior Craftsmanship</h2>
        <p>Don't settle for satisfactory. Our team is committed to the highest standards of excellence every step of the way. Trust us when we say that we'll make you smile.</p></div>
      </article>
    </div>

    <div class="feature-photo" role="img" aria-label="Photo of a modern kitchen flooded with water"></div>

    <p class="tagline">Here for you, every step of the way.</p>
    <p class="contact">P-H-Restoration.com &nbsp;|&nbsp; 803.417.9056</p>

    <div class="brand"><span class="brand-mark"></span>P&amp;H Restoration</div>
  </section>

</main>
</body>
</html>
```